PowerPoint template for online medical education

Need a PowerPoint design for our online urgent care education content Need a title page and then further pages.

must have our logo, name and tagline Academy of Rapid Clinical Practice
Elevating Standards, Shaping Rapid Care
Should match our logo colors scheme

enclosed our logo, tagline ans a copy of our newsletter

Target Market(s)

PHYSICIANS, and other professionals

Industry/Entity Type

Medicine

Font styles to use
Serif

Requirements
Must have
• our logo
• tagline
• color scheme like our logo
Should not have
• too much on content pages

```html
<!DOCTYPE html>
<html lang="en">
<head>
<meta charset="utf-8">
<title>Academy of Rapid Clinical Practice – Presentation Template</title>
<link rel="stylesheet" href="https://fonts.googleapis.com/css2?family=PT+Sans:wght@400;700&family=Libre+Baskerville:ital@1&display=swap">
<style>
  :root {
    --stage-top: #6d6f73;
    --stage-bottom: #a9aaae;
    --orange-light: #ffb347;
    --orange-mid: #f39a3c;
    --orange-deep: #e2572a;
    --ink: #111111;
    --brand-grey: #8c8c8c;
    --tagline-red: #e0352b;
    --white: #ffffff;
    --paper-grey: #e9e9e9;
  }
  * { box-sizing: border-box; margin: 0; padding: 0; }
  html, body { width: 1200px; height: 1200px; overflow: hidden; }
  body {
    position: relative;
    background: linear-gradient(160deg, var(--stage-top) 0%, #8d8f93 55%, var(--stage-bottom) 100%);
    font-family: "PT Sans", Arial, sans-serif;
    color: var(--ink);
  }
  .slide {
    position: absolute;
    width: 485px;
    height: 272px;
    overflow: hidden;
    background: var(--white);
    box-shadow: 14px 14px 30px rgba(0,0,0,0.18);
  }
  .col-left { left: 91px; }
  .col-right { left: 634px; }
  .row-1 { top: 121px; }
  .row-2 { top: 472px; }
  .row-3 { top: 806px; }

  .brand {
    position: absolute;
    display: flex;
    align-items: center;
    gap: 6px;
  }
  .brand-dot {
    width: 14px; height: 14px; border-radius: 50%;
    background: var(--orange-mid);
    flex: none;
  }
  .brand-name {
    font-size: 7.5px;
    line-height: 9px;
    letter-spacing: 0.6px;
    text-transform: uppercase;
    color: var(--brand-grey);
    font-weight: 400;
  }
  .brand--light .brand-dot { background: var(--white); }
  .brand--light .brand-name { color: var(--white); }

  .tagline {
    position: absolute;
    right: 24px;
    font-family: "Libre Baskerville", Georgia, serif;
    font-style: italic;
    color: var(--tagline-red);
    white-space: nowrap;
  }
  .tagline--tiny { font-size: 4.6px; top: 28px; }
  .tagline--small { font-size: 6.6px; top: 21px; }

  .slide-title {
    position: absolute;
    left: 0; right: 0;
    text-align: center;
    font-weight: 400;
  }
  .body-copy {
    position: absolute;
    font-size: 8px;
    line-height: 11.3px;
    text-align: justify;
  }

  /* Slide 1: title */
  .slide--title { background: linear-gradient(180deg, var(--white) 40%, var(--paper-grey) 100%); }
  .slide--title .brand { left: 50%; transform: translateX(-50%); top: 32px; }
  .slide--title .slide-title { top: 124px; font-size: 26px; }
  .band-bottom {
    position: absolute; left: 0; right: 0; bottom: 0;
    background: linear-gradient(180deg, var(--orange-light), var(--orange-deep));
  }
  .slide--title .band-bottom { height: 46px; }

  /* Slide 2: content */
  .slide--content .brand { left: 43px; top: 19px; }
  .slide--content .slide-title { top: 88px; font-size: 21px; }
  .slide--content .body-copy { left: 51px; width: 382px; top: 150px; }
  .slide--content .band-bottom { height: 22px; background: linear-gradient(180deg, var(--orange-light), #f0782f); }

  /* Slide 3: section divider */
  .slide--section { background: linear-gradient(180deg, #f6bd66 0%, var(--orange-mid) 50%, #e16e45 100%); }
  .section-pattern { position: absolute; inset: 0; background: radial-gradient(ellipse at 55% 45%, rgba(255,255,255,0.12), rgba(255,255,255,0) 65%); }
  .slide--section .slide-title { top: 126px; font-size: 26px; color: var(--white); }

  /* Slide 4: sidebar content */
  .sidebar {
    position: absolute; left: 0; top: 0; bottom: 0; width: 158px;
    background: linear-gradient(180deg, var(--orange-light) 0%, var(--orange-mid) 50%, var(--orange-deep) 100%);
  }
  .sidebar .brand { left: 16px; top: 118px; }
  .slide--sidebar .slide-title { left: 158px; top: 58px; font-size: 21px; }
  .slide--sidebar .body-copy { left: 192px; width: 255px; top: 117px; }

  /* Slide 5: two columns */
  .slide--columns .brand { left: 18px; top: 22px; }
  .columns-panel {
    position: absolute; left: 0; right: 0; top: 72px; bottom: 0;
    background: linear-gradient(180deg, var(--orange-light) 0%, var(--orange-mid) 50%, var(--orange-deep) 100%);
  }
  .columns-panel .body-copy { color: var(--white); width: 176px; top: 52px; }
  .columns-panel .body-copy:first-child { left: 29px; }
  .columns-panel .body-copy:last-child { left: 265px; }

  /* Slide 6: photo */
  .photo-area {
    position: absolute; left: 0; right: 0; top: 0; height: 222px;
    background: linear-gradient(100deg, #c9ced3 0%, #e9e3dc 45%, #d9b48e 75%, #c6c9cc 100%);
  }
  .photo-band {
    position: absolute; left: 0; right: 0; bottom: 0; height: 50px;
    background: linear-gradient(180deg, var(--orange-light), #e8704a);
  }
  .photo-band .slide-title { left: 26px; right: auto; top: 10px; font-size: 22px; color: var(--white); text-align: left; }
</style>
</head>
<body>

  <section class="slide slide--title col-left row-1">
    <div class="brand"><span class="brand-dot"></span><span class="brand-name">Academy of<br>Rapid Clinical<br>Practice</span></div>
    <h1 class="slide-title">Lorem ipsum</h1>
    <div class="band-bottom"></div>
  </section>

  <section class="slide slide--content col-right row-1">
    <div class="brand"><span class="brand-dot"></span><span class="brand-name">Academy of<br>Rapid Clinical<br>Practice</span></div>
    <p class="tagline tagline--tiny">Elevating Standards, Shaping Rapid Care</p>
    <h2 class="slide-title">Lorem ipsum</h2>
    <p class="body-copy">Lorem ipsum dolor sit amet, consectetuer adipiscing elit, sed diam nonummy nibh euismod tincidunt ut laoreet dolore magna aliquam erat volutpat. Ut wisi enim ad minim veniam, quis nostrud exerci tation ullamcorper suscipit lobortis nisl ut aliquip ex ea commodo consequat. Duis autem vel eum iriure dolor in hendrerit in vulputate velit esse molestie consequat, vel illum dolore eu feugiat nulla facilisis at vero eros et accumsan et iusto odio dignissim qui blandit</p>
    <div class="band-bottom"></div>
  </section>

  <section class="slide slide--section col-left row-2">
    <div class="section-pattern" role="img" aria-label="Faint honeycomb pattern of medical icons in orange tones"></div>
    <h2 class="slide-title">Lorem ipsum</h2>
  </section>

  <section class="slide slide--sidebar col-right row-2">
    <div class="sidebar">
      <div class="brand brand--light"><span class="brand-dot"></span><span class="brand-name">Academy of<br>Rapid Clinical<br>Practice</span></div>
    </div>
    <p class="tagline tagline--small">Elevating Standards, Shaping Rapid Care</p>
    <h2 class="slide-title">Lorem ipsum</h2>
    <p class="body-copy">Lorem ipsum dolor sit amet, consectetuer adipiscing elit, sed diam nonummy nibh euismod tincidunt ut laoreet dolore magna aliquam erat volutpat. Ut wisi enim ad minim veniam, quis nostrud exerci tation ullamcorper suscipit lobortis nisl ut aliquip ex ea commodo consequat. Duis autem vel eum iriure dolor in hendrerit in vulputate velit esse molestie consequat, vel illum dolore eu feugiat nulla facilisis at vero eros et accumsan et iusto odio dignissim qui blandit</p>
  </section>

  <section class="slide slide--columns col-left row-3">
    <div class="brand"><span class="brand-dot"></span><span class="brand-name">Academy of<br>Rapid Clinical<br>Practice</span></div>
    <p class="tagline tagline--tiny">Elevating Standards, Shaping Rapid Care</p>
    <div class="columns-panel">
      <p class="body-copy">Lorem ipsum dolor sit amet, consectetuer adipiscing elit, sed diam nonummy nibh euismod tincidunt ut laoreet dolore magna aliquam erat volutpat. Ut wisi enim ad minim veniam, quis nostrud exerci tation ullamcorper suscipit lobortis nisl ut aliquip ex ea commodo consequat. Duis autem vel eum iriure dolor in hendrerit in vulputate velit esse molestie consequat, vel illum dolore eu</p>
      <p class="body-copy">Lorem ipsum dolor sit amet, consectetuer adipiscing elit, sed diam nonummy nibh euismod tincidunt ut laoreet dolore magna aliquam erat volutpat. Ut wisi enim ad minim veniam, quis nostrud exerci tation ullamcorper suscipit lobortis nisl ut aliquip ex ea commodo consequat. Duis autem vel eum iriure dolor in hendrerit in vulputate velit esse molestie consequat, vel illum dolore eu</p>
    </div>
  </section>

  <section class="slide slide--photo col-right row-3">
    <div class="photo-area" role="img" aria-label="Photo of a smiling team of doctors and nurses in a clinic"></div>
    <div class="photo-band"><h2 class="slide-title">Lorem ipsum</h2></div>
  </section>

</body>
</html>
```